Business broker needs designs for business card, letterhead and email signature

I require the following items:
- business cards
- letterhead
- email signature

My company is a Business Broker company that specialises in business sales across various industries. The company has branches in four areas and each area has its own logo and website. Initially for the submission I am happy to inspect 1 design and 1 layout for quillharborgroup but the winner will need to complete a design for each area.

The four areas are:
1. quillharborgroup
2. tealridgefuelsales
3. orbvalechainsales
4. pondgrovegrocerdeals

I would like one design for each of the above items for each area. In each design, there should be one prominent logo and then the remaining three should also be included, for eg, the letterhead for the quillharborgrp area would have the quillharborgrp logo featuring prominently, somewhere at the top perhaps and the logos of the other three areas would be smaller and perhaps at the bottom, down the side, etc.

For the business cards, one prominent logo should feature on one side with the remaining three logos on the reverse.

The overall objective is for each item to look like it belongs to one family . I need all the source files as I may add new industries moving forward.

Target Market(s)

My company targets business minded people looking to increase wealth,. make an investment or migrate to Australia. People who busy and are looking for efficient and professional service in securing their next business venture.

Industry/Entity Type

Business

Font styles to use
Serif
Sans Serif

Requirements
Must have
• I want something professional and corporate looking, not something cartoony or playful. I am happy for you to be creative.

```html
<!DOCTYPE html>
<html lang="en">
<head>
<meta charset="utf-8">
<title>Quillharborgroup Letterhead</title>
<link rel="stylesheet" href="https://fonts.googleapis.com/css2?family=Roboto+Condensed:wght@700&family=Jost:wght@400&display=swap">
<style>
  :root {
    --ink: #343e49;
    --red: #c52034;
    --orange: #f5a21f;
    --green: #7ac143;
    --teal: #2bbfa4;
    --paper: #ffffff;
    --text: #2b2f36;
  }
  html, body {
    margin: 0;
    padding: 0;
    width: 848px;
    height: 1200px;
    overflow: hidden;
    background: var(--paper);
  }
  .letterhead {
    position: relative;
    width: 919px;
    height: 1300px;
    transform: scale(0.92274);
    transform-origin: 0 0;
    background: var(--paper);
  }
  .corner-shapes {
    position: absolute;
    inset: 0;
    width: 919px;
    height: 1300px;
  }
  .brand-main {
    position: absolute;
    left: 126px;
    top: 64px;
    display: flex;
    align-items: center;
    gap: 12px;
  }
  .brand-main .mark {
    width: 50px;
    height: 50px;
    border-radius: 50%;
    background: var(--ink);
  }
  .brand-main .name {
    font-family: "Roboto Condensed", "Arial Narrow", sans-serif;
    font-weight: 700;
    font-size: 40px;
    letter-spacing: -0.5px;
    color: var(--ink);
    line-height: 1;
  }
  .brand-family {
    position: absolute;
    left: 690px;
    top: 46px;
    margin: 0;
    padding: 0;
    list-style: none;
  }
  .brand-family li {
    display: flex;
    align-items: center;
    gap: 7px;
    height: 22px;
    margin-bottom: 14.5px;
    font-family: "Roboto Condensed", "Arial Narrow", sans-serif;
    font-weight: 700;
    font-size: 16px;
    color: var(--ink);
  }
  .brand-family .dot {
    width: 19px;
    height: 19px;
    border-radius: 50%;
  }
  .dot.franchise { background: var(--orange); }
  .dot.grocer { background: var(--green); }
  .dot.fuel { background: var(--teal); }
  .footer-contact {
    position: absolute;
    top: 1227px;
    font-family: "Jost", "Futura", sans-serif;
    font-size: 16px;
    line-height: 21px;
    color: var(--text);
  }
  .footer-contact p { margin: 0; }
  .footer-contact.online { left: 32px; }
  .footer-contact.office { left: 330px; }
</style>
</head>
<body>
  <div class="letterhead">
    <svg class="corner-shapes" viewBox="0 0 919 1300" aria-hidden="true">
      <polygon points="40,0 138,0 70,66" fill="var(--red)"/>
      <polygon points="0,16 0,136 63,74" fill="var(--ink)"/>
      <polygon points="781,1156 919,1017 919,1296" fill="var(--ink)"/>
      <polygon points="635,1300 773,1162 911,1300" fill="var(--red)"/>
    </svg>

    <header class="brand-main">
      <span class="mark"></span>
      <span class="name">quillharborgroup</span>
    </header>

    <ul class="brand-family">
      <li><span class="dot franchise"></span>orbvalechainsales</li>
      <li><span class="dot grocer"></span>pondgrovegrocerdeals</li>
      <li><span class="dot fuel"></span>tealridgefuelsales</li>
    </ul>

    <footer>
      <div class="footer-contact online">
        <p>info@quillharborgroup.com</p>
        <p>&nbsp;www.quillharborgroup.com</p>
      </div>
      <div class="footer-contact office">
        <p>Calder 18 20417, P.O Box 3082</p>
        <p>+000 000 0 000</p>
      </div>
    </footer>
  </div>
</body>
</html>
```